Business Card for innovative, tech/consultant company

We are specializing in bringing together Efficiency methodology and Technology for our Business customers. We would like an astonishing business Card that matches this idea.

Target Market(s)

Businesses of medium size or more

Industry/Entity Type

Business Consultant

Contact Information for Business Card

Name, Title, personal email, www, address, phone

Font styles to use
Sans Serif

Colors
3277b5

Requirements
Must have
• - innovative, efficient design
• - good readable
• - Colors must match our logo (blue and grey)
• - the attached font (is licensed by our Company) must be used (Syntax LT)
Should not have
• overloaded

```html
<!DOCTYPE html>
<html lang="en">
<head>
<meta charset="utf-8">
<title>Veyra Business Card</title>
<link rel="stylesheet" href="https://fonts.googleapis.com/css2?family=Hind:wght@400;500&display=swap">
<style>
  :root {
    --backdrop: #e6e4e1;
    --card: #f7f6f3;
    --brand-blue: #1a86c4;
    --brand-grey: #838383;
    --ink: #1e1e1e;
  }
  * { margin: 0; padding: 0; box-sizing: border-box; }
  html, body {
    width: 1200px;
    height: 857px;
    overflow: hidden;
    background: var(--backdrop);
    font-family: "Hind", sans-serif;
  }
  .card {
    position: absolute;
    left: 150px;
    top: 171px;
    width: 900px;
    height: 514px;
    background: var(--card);
    box-shadow: 0 6px 18px rgba(0,0,0,0.15);
    overflow: hidden;
  }
  .accent-bar {
    position: absolute;
    background: var(--brand-blue);
    border-radius: 14px;
  }
  .accent-bar--left { left: 24px; top: 160px; width: 110px; height: 330px; }
  .accent-bar--right { right: 22px; top: 36px; width: 120px; height: 300px; }
  .card-content {
    position: absolute;
    left: 180px;
    right: 180px;
    top: 60px;
    text-align: center;
    color: var(--ink);
  }
  .brand-name {
    font-size: 118px;
    font-weight: 400;
    line-height: 1;
    color: var(--brand-grey);
    letter-spacing: 1px;
  }
  .person-name { margin-top: 14px; font-size: 32px; font-weight: 500; line-height: 1.05; }
  .person-title { font-size: 26px; line-height: 1.1; }
  .contact-list { list-style: none; margin-top: 46px; font-size: 26px; line-height: 1.2; }
</style>
</head>
<body>
  <main class="card">
    <div class="accent-bar accent-bar--left"></div>
    <div class="accent-bar accent-bar--right"></div>
    <section class="card-content">
      <h1 class="brand-name">Veyra</h1>
      <p class="person-name">J. Alan Porter</p>
      <p class="person-title">Director</p>
      <ul class="contact-list">
        <li>555-014-2280</li>
        <li>hello@veyra.com</li>
        <li>www.veyra.com</li>
        <li>PO Box 512, Elmcrest 4870 Northland AU</li>
      </ul>
    </section>
  </main>
</body>
</html>
```